Velmora and Co Business Card Design

Looking for a business card design. Wanting Smart, Clean and Sharp looking to promote Velmora and Co, our Import Export Business - like Black, White and natural textures. I have uploaded our logo. I like a rounded font but open to other ideas
Being that we have a wide range of products on offer we are looking for a neutral yet eye catching card. We would also like to have Import - Export on the business card to be clear on want our business does.

Target Market(s)

Import export market

Industry/Entity Type

Importer

Contact Information for Business Card

Mr Tobias Kernwell
tobias.kernwell@velmoraandco.com.au
+61 (0) 417 630 284
www.velmoraandco.com.au

Font styles to use
Other font styles liked:
• Unsure of actual font name but something rounded and clean

Colors

Designer to choose colors to be used in the design.

Requirements
Must have
• Instagram icon
• Facebook icon

```html
<!DOCTYPE html>
<html lang="en">
<head>
<meta charset="utf-8">
<title>Velmora and Co – Business Card</title>
<link href="https://fonts.googleapis.com/css2?family=Exo+2:wght@400;500;600&display=swap" rel="stylesheet">
<style>
  :root {
    --ink: #231f20;
    --paper: #ffffff;
    --font: "Exo 2", sans-serif;
  }
  * { box-sizing: border-box; margin: 0; padding: 0; }
  html, body { width: 957px; height: 1200px; overflow: hidden; background: var(--paper); }
  body { font-family: var(--font); color: var(--ink); position: relative; }

  .card-front { position: absolute; left: 0; top: 0; width: 957px; height: 653px; background: var(--paper); }
  .card-back { position: absolute; left: 0; top: 653px; width: 957px; height: 547px; background: var(--ink); }

  .brand-name {
    position: absolute;
    font-family: var(--font);
    font-weight: 600;
    text-transform: uppercase;
    line-height: 0.95;
    letter-spacing: 0.5px;
  }
  .front-brand { left: 69px; top: 120px; font-size: 46px; color: var(--ink); }
  .back-brand { left: 0; width: 957px; top: 840px; font-size: 58px; color: var(--paper); text-align: center; }

  .person-name {
    position: absolute; right: 68px; top: 242px;
    font-size: 40px; font-weight: 400; line-height: 1;
  }
  .title-bar {
    position: absolute; left: 69px; top: 291px; width: 820px; height: 21px;
    background: var(--ink);
  }
  .person-title {
    position: absolute; right: 2px; top: -2px;
    font-size: 22px; line-height: 1; color: var(--paper);
  }

  .contact-list { position: absolute; left: 0; top: 327px; list-style: none; }
  .contact-item {
    position: relative; height: 40.5px; padding-left: 145px;
    font-size: 23px; font-weight: 500; line-height: 34px;
  }
  .contact-icon { position: absolute; top: 7px; }
  .icon-single { left: 99px; }
  .icon-pair { left: 69px; }

  .tagline {
    position: absolute; left: 0; top: 1088px; width: 957px;
    text-align: center; color: var(--paper);
    font-size: 40px; font-weight: 400; line-height: 1;
  }
</style>
</head>
<body>
  <section class="card-front">
    <div class="brand-name front-brand">Velmora<br>&amp; Co</div>

    <h1 class="person-name">Mr. Tobias Kernwell</h1>
    <div class="title-bar"><span class="person-title">Founder &amp; CEO</span></div>

    <ul class="contact-list">
      <li class="contact-item">
        <svg class="contact-icon icon-single" width="26" height="26" viewBox="0 0 26 26" aria-hidden="true">
          <circle cx="13" cy="13" r="12" fill="#231f20"/>
          <path d="M9 7.5c.6-.6 1.4-.5 1.8.1l1.2 1.9c.3.5.2 1.1-.2 1.5l-.8.7c.6 1.4 1.8 2.6 3.2 3.2l.7-.8c.4-.4 1-.5 1.5-.2l1.9 1.2c.6.4.7 1.2.1 1.8l-.9.9c-.8.8-2.1.9-3.3.3-2.9-1.4-4.8-3.4-6.2-6.2-.6-1.2-.5-2.5.3-3.3z" fill="#fff"/>
        </svg>
        +61 (0) 417 630 284
      </li>
      <li class="contact-item">
        <svg class="contact-icon icon-pair" width="56" height="26" viewBox="0 0 56 26" aria-hidden="true">
          <circle cx="13" cy="13" r="12" fill="#231f20"/>
          <circle cx="43" cy="13" r="12" fill="#231f20"/>
        </svg>
        @tobias.kernwell
      </li>
      <li class="contact-item">
        <svg class="contact-icon icon-single" width="26" height="26" viewBox="0 0 26 26" aria-hidden="true">
          <circle cx="13" cy="13" r="12" fill="#231f20"/>
          <rect x="7" y="8.5" width="12" height="9" rx="1.2" fill="none" stroke="#fff" stroke-width="1.6"/>
          <path d="M7.5 9.5l5.5 4.2 5.5-4.2" fill="none" stroke="#fff" stroke-width="1.6"/>
        </svg>
        tobias.kernwell@velmoraandco.com.au
      </li>
      <li class="contact-item">
        <svg class="contact-icon icon-single" width="26" height="26" viewBox="0 0 26 26" aria-hidden="true">
          <circle cx="13" cy="13" r="12" fill="#231f20"/>
          <circle cx="13" cy="13" r="7" fill="none" stroke="#fff" stroke-width="1.5"/>
          <ellipse cx="13" cy="13" rx="3" ry="7" fill="none" stroke="#fff" stroke-width="1.3"/>
          <path d="M6 13h14" stroke="#fff" stroke-width="1.3"/>
        </svg>
        www.velmoraandco.com.au
      </li>
    </ul>
  </section>

  <section class="card-back"></section>
  <div class="brand-name back-brand">Velmora<br>&amp; Co</div>
  <p class="tagline">Import-Export</p>
</body>
</html>
```